Elite Academic Day-care program needs to develop a Vision board poster with Famous Montessori Alu...

The core of our vision is to develop leaders that better the world. We want to demonstrate this vision by identifying and associating famous Montessori alumni with our program. We want parents to understand that they are enrolling in an elite program that will unequivocally prepare their children for life. I would like to be able to print large posters (36 x 24 inch) for display. We have done some work to date but the format is bland, the images are out of scale and become too grainy when enlarged. I want something that speaks to our vision.

Target Market(s)

Parents of daycare and preschool aged children.

Colors

Designer to choose colors to be used in the design.

Requirements
Must have
• Need Title: Maple Crest Preschool. I want the main focus to be our vision statement "We will be the school that develops leaders and citizens that better the world"
• Third line saying: Montessori Alumni
• I want two posters with the same vision statement but with a different set of 10 pictures. ( see attachment)
Nice to have
• I have attached the logo but it is old and of poor quality so likely will not work.

```html
<!DOCTYPE html>
<html lang="en">
<head>
<meta charset="utf-8">
<title>Vision Board Poster</title>
<link rel="stylesheet" href="https://fonts.googleapis.com/css2?family=Fira+Sans+Condensed:wght@600;700&family=PT+Sans+Narrow&display=swap">
<style>
  :root {
    --page: #e9e6ec;
    --teal: #3fb4c6;
    --blue: #2c3c9f;
    --deep-blue: #262f8a;
    --magenta: #d4217e;
    --magenta-dark: #9c1759;
    --magenta-shade: #6e0f3e;
    --white: #ffffff;
  }
  * { margin: 0; padding: 0; box-sizing: border-box; }
  html, body { width: 842px; height: 1200px; overflow: hidden; background: var(--page); }
  .canvas { position: relative; width: 842px; height: 1200px; }
  .poster {
    position: absolute; left: 0; top: 290px; width: 842px; height: 620px; overflow: hidden;
    background:
      radial-gradient(ellipse at 15% 10%, rgba(120,220,225,.55), transparent 55%),
      linear-gradient(135deg, var(--teal) 0%, #3a86bd 40%, var(--blue) 75%, var(--deep-blue) 100%);
  }
  .school-name {
    position: absolute; left: 0; top: 16px; width: 842px; text-align: center;
    color: var(--white); font-family: "Fira Sans Condensed", sans-serif; font-weight: 700;
    font-size: 30px; line-height: 36px; letter-spacing: 2px;
    text-shadow: 0 2px 4px rgba(0,0,0,.25);
  }
  .ribbons { position: absolute; left: 0; top: 42px; width: 842px; height: 150px; }
  .vision {
    position: absolute; color: var(--white); background: var(--magenta);
    font-family: "Fira Sans Condensed", sans-serif; font-weight: 700;
    font-size: 30px; letter-spacing: .5px; text-align: center; line-height: 46px; height: 46px;
    box-shadow: 0 2px 4px rgba(0,0,0,.25); white-space: nowrap;
  }
  .vision-one { left: 44px; top: 70px; width: 722px; }
  .vision-two { left: 111px; top: 124px; width: 590px; }
  .alumni-heading {
    position: absolute; left: 0; top: 190px; width: 842px; text-align: center;
    color: var(--white); font-family: "Fira Sans Condensed", sans-serif; font-weight: 600;
    font-size: 20px; line-height: 24px; letter-spacing: 4px;
  }
  .alumni {
    position: absolute; left: 20px; top: 228px;
    display: grid; grid-template-columns: repeat(5, 145px); grid-auto-rows: 173px;
    column-gap: 16.5px; row-gap: 18px;
  }
  .card {
    background: var(--magenta); border-radius: 8px; padding: 0 3px;
    display: flex; flex-direction: column; box-shadow: 0 3px 6px rgba(0,0,0,.3);
  }
  .card-name {
    height: 29px; line-height: 30px; text-align: center; color: var(--white);
    font-family: "Fira Sans Condensed", sans-serif; font-weight: 700; font-size: 17px;
    white-space: nowrap; letter-spacing: .2px;
  }
  .card-name.tight { font-size: 12.5px; letter-spacing: -.3px; }
  .portrait { flex: 1; }
  .card-role {
    height: 22px; line-height: 22px; text-align: center; color: var(--white);
    font-family: "PT Sans Narrow", sans-serif; font-size: 12.5px; letter-spacing: .4px; white-space: nowrap;
  }
  .card-role.tight { font-size: 11.5px; letter-spacing: 0; }
  .tone-sepia { background: linear-gradient(160deg, #3b2f28, #7a6a5c 55%, #2b211b); }
  .tone-warm  { background: linear-gradient(160deg, #d9d3c9, #c9a98a 50%, #8f93a8); }
  .tone-red   { background: linear-gradient(160deg, #8e1d1d, #c0584a 50%, #3a2f42); }
  .tone-dark  { background: linear-gradient(160deg, #2a2a2e, #8a6a52 50%, #1f2b44); }
  .tone-grey  { background: linear-gradient(160deg, #9a9a98, #b08c74 50%, #1d2c52); }
  .tone-black { background: linear-gradient(160deg, #cfcfcf, #b9916f 45%, #141414); }
  .tone-gold  { background: linear-gradient(160deg, #d8c6ad, #b47f57 50%, #e3c7c0); }
  .tone-mono  { background: linear-gradient(160deg, #cfcfcf, #6e6e6e 50%, #e8e8e8); }
  .tone-rose  { background: linear-gradient(160deg, #3a2a3a, #a5553a 45%, #e6c0b2); }
  .tone-slate { background: linear-gradient(160deg, #5a5a5c, #8b6d55 50%, #1f2d55); }
</style>
</head>
<body>
<div class="canvas">
  <section class="poster">
    <p class="school-name">MAPLE CREST PRESCHOOL</p>
    <svg class="ribbons" viewBox="0 0 842 150" aria-hidden="true">
      <polygon points="742,10 800,10 790,26 800,42 766,42 766,28" fill="var(--magenta-dark)"/>
      <polygon points="742,10 766,28 766,42" fill="var(--magenta-shade)"/>
      <polygon points="92,112 111,112 111,127 150,127 135,145 90,145 100,128" fill="var(--magenta-dark)"/>
    </svg>
    <h1 class="vision vision-one">WE WILL BE THE SCHOOL THAT DEVELOPS LEADERS</h1>
    <h2 class="vision vision-two">AND CITIZENS THAT BETTER THE WORLD</h2>
    <p class="alumni-heading">MONTESSORI ALUMNI</p>

    <div class="alumni">
      <article class="card"><h3 class="card-name">ELLIS MARROW</h3><div class="portrait tone-sepia" role="img" aria-label="Portrait photograph of Ellis Marrow"></div><p class="card-role">Famous Inventor</p></article>
      <article class="card"><h3 class="card-name">NORA HALLIDAY</h3><div class="portrait tone-warm" role="img" aria-label="Portrait photograph of Nora Halliday"></div><p class="card-role tight">Former Secretary of State</p></article>
      <article class="card"><h3 class="card-name tight">OWEN PRATT / ILYA BROM</h3><div class="portrait tone-red" role="img" aria-label="Photograph of the two founders"></div><p class="card-role">Founders of Searchly</p></article>
      <article class="card"><h3 class="card-name">DARIUS COLE</h3><div class="portrait tone-dark" role="img" aria-label="Portrait photograph of Darius Cole"></div><p class="card-role tight">MVP &amp; League Champion</p></article>
      <article class="card"><h3 class="card-name">MARTIN VALE</h3><div class="portrait tone-grey" role="img" aria-label="Portrait photograph of Martin Vale"></div><p class="card-role">Founder of Rivermart</p></article>

      <article class="card"><h3 class="card-name">JONAH REED</h3><div class="portrait tone-black" role="img" aria-label="Portrait photograph of violinist Jonah Reed"></div><p class="card-role tight">Laurel Award Winning Violinist</p></article>
      <article class="card"><h3 class="card-name">SELENE</h3><div class="portrait tone-gold" role="img" aria-label="Portrait photograph of singer Selene"></div><p class="card-role">Singer / Actress</p></article>
      <article class="card"><h3 class="card-name">IRIS KENDALL</h3><div class="portrait tone-mono" role="img" aria-label="Black and white portrait of Iris Kendall"></div><p class="card-role tight">Author, Activist &amp; Lecturer</p></article>
      <article class="card"><h3 class="card-name">QUEEN AMARA</h3><div class="portrait tone-rose" role="img" aria-label="Portrait photograph of Queen Amara"></div><p class="card-role tight">Queen Dowager of Veloria</p></article>
      <article class="card"><h3 class="card-name">LIN HAO</h3><div class="portrait tone-slate" role="img" aria-label="Portrait photograph of cellist Lin Hao"></div><p class="card-role">World famous Cellist</p></article>
    </div>
  </section>
</div>
</body>
</html>
```